Consulting Firm of Business Savvy Super Geeks Needs Business Cards Redesigned

We need our business cards redesigned to reflect the company branding better, especially the website: www.TrelvoAdvisory.com . Note the phrase "Clear Strategy. Sharper Systems" from the website. Also would love to see options that include verbiage of our offerings: Cloud Solutions, Digital Workspace, CRM Services, Quandrel Partner, Security Services, ERP Services.

Industry/Entity Type

Consulting

Contact Information for Business Card

Direct Phone #, Cell Phone #, Linkedin Address, Web address, Office Address

Font styles to use
Sans Serif

Requirements
Must have
• The cards should reflect the website.
• Clean design.
Nice to have
• Mentions to each of the business units / practices mentioned in the description.

```html
<!DOCTYPE html>
<html lang="en">
<head>
<meta charset="utf-8">
<title>Trelvo Advisory – Business Cards</title>
<link href="https://fonts.googleapis.com/css2?family=Fira+Sans:ital,wght@0,400;0,600;0,800;1,400&family=Jost:wght@400;500&display=swap" rel="stylesheet">
<style>
  :root {
    --bg: #d9dbe0;
    --card-white: #ffffff;
    --card-black: #121315;
    --card-black-2: #24262a;
    --ink: #1b1b1d;
    --royal: #1f46a8;
    --sky: #3e9fe2;
    --sky-soft: #7cc2ef;
    --paper-text: #f4f6f9;
  }
  * { box-sizing: border-box; margin: 0; padding: 0; }
  html, body {
    width: 1200px; height: 900px; overflow: hidden;
    background: var(--bg);
    font-family: "Fira Sans", Arial, sans-serif;
  }
  .stage {
    width: 1200px; height: 900px;
    display: flex; flex-direction: column;
    align-items: center; justify-content: center; gap: 44px;
  }
  .card {
    position: relative;
    width: 680px; height: 388px;
    border-radius: 24px;
    overflow: hidden;
    box-shadow: 0 10px 28px rgba(0,0,0,.18);
  }

  /* Front */
  .card-front { background: var(--card-white); color: var(--ink); }
  .card-front .edge-band {
    position: absolute; right: 0; top: 0; bottom: 0; width: 38px;
    background: var(--royal);
  }
  .person { position: absolute; left: 44px; top: 38px; }
  .person-name { font-size: 30px; font-weight: 600; color: var(--royal); line-height: 1.1; }
  .person-role { font-size: 17px; margin-top: 4px; }
  .person-rule { width: 26px; height: 4px; background: var(--royal); margin-top: 14px; }
  .contact {
    position: absolute; left: 44px; top: 160px;
    font-size: 17px; line-height: 1.3;
  }
  .contact .gap { margin-top: 12px; }
  .brand {
    position: absolute; left: 352px; top: 150px;
    display: flex; align-items: center; gap: 10px;
  }
  .brand-name { font-size: 36px; font-weight: 800; color: var(--ink); letter-spacing: -0.5px; white-space: nowrap; }
  .brand-square { width: 18px; height: 18px; background: var(--sky); flex: none; }
  .address {
    position: absolute; right: 74px; bottom: 36px;
    font-size: 20px; line-height: 1.3; text-align: left;
  }

  /* Back */
  .card-back {
    background: linear-gradient(125deg, var(--card-black-2) 0%, var(--card-black) 55%, #1b1c1f 100%);
    color: var(--paper-text);
  }
  .card-back .edge-band {
    position: absolute; left: 0; top: 0; bottom: 0; width: 26px;
    background: var(--sky);
  }
  .back-brand { position: absolute; left: 70px; top: 56px; }
  .back-brand .brand-row { display: flex; align-items: center; gap: 12px; }
  .back-brand .brand-name { color: var(--paper-text); font-size: 56px; }
  .back-brand .brand-square { width: 24px; height: 24px; }
  .tagline {
    font-size: 15px; font-style: italic; color: var(--sky-soft);
    margin-top: 2px; letter-spacing: .2px;
  }
  .services {
    position: absolute; left: 400px; top: 86px;
    list-style: none;
    font-family: "Jost", "Futura", sans-serif; font-size: 21px; font-weight: 500;
  }
  .services li { display: flex; align-items: center; gap: 12px; line-height: 1.7; }
  .services li::before {
    content: ""; width: 12px; height: 12px; background: var(--sky); flex: none;
  }
</style>
</head>
<body>
<main class="stage">
  <section class="card card-front" aria-label="Business card front">
    <div class="person">
      <p class="person-name">Dana Morell</p>
      <p class="person-role">CEO</p>
      <div class="person-rule"></div>
    </div>
    <div class="contact">
      <p>Office: 555 201 0394</p>
      <p>Direct: 555 201 0237</p>
      <p>Cell: 555 304 7719</p>
      <p class="gap">dana.morell@trelvoadvisory.com</p>
      <p>TrelvoAdvisory.com</p>
    </div>
    <div class="brand">
      <span class="brand-name">Trelvo Advisory</span>
      <span class="brand-square"></span>
    </div>
    <p class="address">218 Larkspur Ave.<br>Denholm, PA 15299</p>
    <div class="edge-band"></div>
  </section>

  <section class="card card-back" aria-label="Business card back">
    <div class="edge-band"></div>
    <div class="back-brand">
      <div class="brand-row">
        <span class="brand-name">Trelvo</span>
        <span class="brand-square"></span>
      </div>
      <p class="tagline">Clear Strategy. Sharper Systems</p>
    </div>
    <ul class="services">
      <li>Cloud Solutions</li>
      <li>Digital Workspace</li>
      <li>CRM Services</li>
      <li>Quandrel Partner</li>
      <li>Security Services</li>
      <li>ERP Services</li>
    </ul>
  </section>
</main>
</body>
</html>
```